Bright oak path business card

Bright oak path is a new online life insurance company providing instant quotes and policies to consumers.
Target Market(s)
Target market is both business to business as well as business to consumer
Can think out side of the box- We are an open minded bunch
Industry/Entity Type
Life Insurance
Requirements
Must have
- Our corporate Logo
Double sided
Website www.brightoakpath.com.au
Phone Number
Name & Position of each person etc.
Modern font

```html
<!DOCTYPE html>
<html lang="en">
<head>
<meta charset="utf-8">
<title>Bright oak path business card</title>
<link rel="stylesheet" href="https://fonts.googleapis.com/css2?family=Crimson+Pro:wght@400;600&display=swap">
<style>
  :root {
    --page: #ffffff;
    --card-tan: #c3b59b;
    --disc-cream: #e7e3d0;
    --ring-white: #ffffff;
    --ink: #2a2624;
    --accent: #ee8a22;
    --dial: #d8cfbd;
  }
  * { margin: 0; padding: 0; box-sizing: border-box; }
  html, body {
    width: 1200px;
    height: 900px;
    overflow: hidden;
    background: var(--page);
  }
  .canvas {
    position: relative;
    width: 1200px;
    height: 900px;
    font-family: "Crimson Pro", Georgia, serif;
    color: var(--ink);
  }
  .card {
    position: absolute;
    top: 64px;
    width: 440px;
    height: 768px;
    background: var(--card-tan);
    overflow: hidden;
  }
  .card--front { left: 88px; }
  .card--back { left: 668px; }
  .card-art {
    position: absolute;
    inset: 0;
    width: 440px;
    height: 768px;
  }
  .brand {
    position: absolute;
    left: 52px;
    top: 268px;
    display: flex;
    align-items: center;
    gap: 14px;
  }
  .brand-dot {
    width: 22px;
    height: 22px;
    border-radius: 50%;
    background: var(--accent);
    flex: none;
  }
  .brand-name {
    font-size: 54px;
    font-weight: 600;
    line-height: 0.95;
    color: var(--ink);
    letter-spacing: -0.5px;
  }
  .person {
    position: absolute;
    right: 48px;
    top: 212px;
    text-align: right;
  }
  .person-name {
    font-size: 34px;
    font-weight: 400;
    line-height: 1;
    letter-spacing: 0.5px;
  }
  .person-role {
    font-size: 18px;
    line-height: 1.3;
  }
  .contact {
    position: absolute;
    left: 124px;
    top: 500px;
    font-size: 18px;
    line-height: 26px;
  }
  .contact-phone { margin-bottom: 8px; }
  .website {
    position: absolute;
    left: 16px;
    bottom: 12px;
    font-size: 18px;
    color: var(--ring-white);
    letter-spacing: 0.3px;
  }
</style>
</head>
<body>
<main class="canvas">

  <section class="card card--front" aria-label="Card front">
    <svg class="card-art" viewBox="0 0 440 768" aria-hidden="true">
      <circle cx="220" cy="272" r="250" fill="var(--disc-cream)" stroke="var(--ring-white)" stroke-width="10"/>
    </svg>
    <svg class="card-art" viewBox="0 0 440 768" role="img" aria-label="Partial clock face decoration in the lower corner">
      <circle cx="402" cy="736" r="130" fill="var(--dial)"/>
    </svg>
    <div class="brand">
      <span class="brand-dot" aria-hidden="true"></span>
      <p class="brand-name">Bright oak<br>path</p>
    </div>
  </section>

  <section class="card card--back" aria-label="Card back">
    <svg class="card-art" viewBox="0 0 440 768" aria-hidden="true">
      <circle cx="222" cy="336" r="260" fill="var(--disc-cream)" stroke="var(--ring-white)" stroke-width="10"/>
    </svg>
    <svg class="card-art" viewBox="0 0 440 768" role="img" aria-label="Partial clock face decoration in the lower corner">
      <circle cx="412" cy="726" r="130" fill="var(--dial)"/>
    </svg>
    <div class="person">
      <p class="person-name">Daniel Marsh</p>
      <p class="person-role">Managing Director</p>
    </div>
    <address class="contact" style="font-style: normal;">
      <p class="contact-phone">phone: 1300 555 014</p>
      <p>Level 12, 45 Carrow Street</p>
      <p>Westbury NSW 2190</p>
    </address>
    <p class="website">www.brightoakpath.com.au</p>
  </section>

</main>
</body>
</html>
```